Smart Routing SaaS needs a magic web design

We need a web design that focuses in the UX and conveys the idea of doing magic through our software. The company name is Brindal and it is a word game about wow and slip... we are a software as a service B2B that helps companies automate dispatches and routes for their delivery guys to deliver goods to the customers. Think of it as an zappa software applicable to your own fleet or third party fleets that can be used for example in a supermarket. That way the final user (buyer of the supermarket) knows where the parcel is, if it is leaving the store, if it is on its way, how long will it take to arrive, who is the delivery guy, etc... Brindal's symbol is an owl. Think of it as the movie The Tinker: Ember's Oath, Queen Odalie had an owl mask and the ice owl who was her eyes on the field... that is the idea I want to convey through this software. It is the eyes for the business and the eyes for the final user. The software is comprised of a web platform (for the business with the fleet to manage) and the driver's application. The final customer receives the real time tracking information through SMS and email. The design should communicate magic through the use of the software... You can see some info on the existing webpage... which is very cold and dull... no life in it brindal.example.. Use of gifs is desirable.

Text that can be used on the cover to convey main idea:

High end technology
We take care of your delivery management

The software that brings visibility and smartness to your deliveries through automated dispatches and smart routings
Our expertise: A Delightful Customer Experience of Deliveries

Target Market(s)

Professionals and businesses of all types with a delivery of any kind (supermarkets, pharmacies, restaurants, moving services, fleets, home services, deliveries, supply chain, field sales...)
Please look at competition webpages:
www.pathkite.example
www.movr.example
www.lanevo.example
tramway.example
gobrisk.example
zappa dash

Business Software

Coded - Design and coding required

5+ page

Other font styles liked:
• Modulus and Trade Gothic Ltd

Requirements
Must have
• MUST HAVE A K7VZ LIKE:
• http://snip.example/kdorvan/4471203
• http://kdorvan.example/k7/talk/20111116/force-collapsible.html
• https://dorv.example/kurt/fisheye/
• http://motionfigs.example/lab/k7-tree/
• A great magic capturing Homepage that conveys the main idea of what we are. A software that will help you manage your people on field who are getting something to the end customer (who will be aware of the live parcel status through SMS/ email notifications), we live in the cloud... no need of implementation fees, there is a free demo. Right now the webpage has an animation. Maybe a picture with a video on it could be something nice, or something that moves... take a look at zappa dash. The main idea of the page should send the idea of something magic... use the owl... something that flies.
• The page must have gifs here and there... never stop the idea of a swift magic going on... efficiency on the logistics management of the company... happy customers.
• Parallax... I love parallax.
Nice to have
• The webpage may be telling a story... first what are we and what we do... how it works, who is our market, the benefits, hard facts on efficiency... please take a look at the current webpage www.brindal.example to get more info but make it beautiful.
• A phrase here and there of why they need our service
Should not have
• I want to change the current idea of the webpage that the software aims only to manage fleets for home delivery... we are NOT a home delivery only management system. We can make any company's logistics "fly".
• I dont want to see dullness in the webpage, I am looking for a soul.

```html
<!DOCTYPE html>
<html lang="en">
<head>
<meta charset="utf-8">
<title>Brindal – Contact</title>
<link href="https://fonts.googleapis.com/css2?family=Roboto:wght@300;400;500;700&display=swap" rel="stylesheet">
<style>
:root{
  --teal:#12a9c6;
  --teal-dark:#0a8aa6;
  --hero-a:#0a5566;
  --hero-b:#1890a8;
  --hero-glow:rgba(120,225,240,.35);
  --ink:#555a5e;
  --muted:#9a9ea2;
  --field:#f8f8f8;
  --line:#dcdcdc;
  --footer:#2a2828;
  --footer-deep:#1c1b1b;
  --white:#ffffff;
}
*{box-sizing:border-box;margin:0;padding:0}
html,body{width:1138px;height:1200px;overflow:hidden}
body{position:relative;background:var(--white);font-family:"Roboto",Arial,sans-serif;color:var(--ink)}
.abs{position:absolute}
.top-rule{left:0;top:0;width:1138px;height:3px;background:var(--teal)}
.brand{left:93px;top:34px;display:flex;align-items:center;gap:6px;font-size:36px;font-weight:300;color:var(--teal);letter-spacing:1px}
.brand-dot{width:8px;height:8px;border-radius:50%;background:var(--teal)}
.nav{left:0;top:49px;width:1138px;font-size:13px;font-weight:300;color:#555}
.nav span{position:absolute;white-space:nowrap}
.nav .active{color:var(--teal)}
.hero{left:0;top:107px;width:1138px;height:294px;
  background:
    radial-gradient(circle at 47% 18%,var(--hero-glow),rgba(0,0,0,0) 22%),
    radial-gradient(circle at 75% 72%,rgba(90,200,225,.3),rgba(0,0,0,0) 28%),
    radial-gradient(circle at 20% 80%,rgba(160,50,50,.25),rgba(0,0,0,0) 20%),
    linear-gradient(135deg,var(--hero-a),var(--hero-b) 60%,#1a9ab3)}
.hero-title{left:0;top:206px;width:1138px;text-align:center;color:#fff;font-weight:700;font-size:41px;text-shadow:0 2px 4px rgba(0,0,0,.35)}
.hero-sub{left:0;top:264px;width:1138px;text-align:center;color:#fff;font-weight:500;font-size:33px;text-shadow:0 2px 4px rgba(0,0,0,.35)}
.hero-arrow{top:235px;width:33px;height:33px}
.hero-shade{left:60px;top:401px;width:1018px;height:30px;background:radial-gradient(ellipse at top,rgba(0,0,0,.12),rgba(0,0,0,0) 70%)}
.section-title{left:93px;top:450px;font-size:29px;font-weight:400;color:#555}
.section-title b{font-weight:400;color:var(--teal)}
.field{background:var(--field);border:1px solid var(--line);font-size:13px;font-weight:300;color:var(--muted);padding:0 15px;display:flex;align-items:center;justify-content:space-between}
.field svg{width:12px;height:12px;fill:#666}
.field.msg{align-items:flex-start;padding-top:14px}
.submit{left:93px;top:854px;width:157px;height:45px;background:linear-gradient(var(--teal),var(--teal-dark));color:#fff;font-size:16px;font-weight:300;display:flex;align-items:center;justify-content:center}
.map{left:710px;top:456px;width:335px;height:212px;border:1px solid #e3e3e3;padding:4px;background:#fff;box-shadow:0 0 3px rgba(0,0,0,.12)}
.map div{width:100%;height:100%;background:linear-gradient(135deg,#e3ecd6,#eef0e8 35%,#e6e8e0 65%,#eceae3)}
.addr-title{left:710px;top:693px;font-size:16px;font-weight:400;color:#444}
.addr-rule{left:710px;top:727px;width:335px;height:1px;background:#e6e6e6}
.addr-item{left:750px;font-size:12.5px;font-weight:300;color:#666;line-height:16px;width:230px}
.addr-icon{left:710px;width:16px;height:16px;fill:none;stroke:var(--teal);stroke-width:1.8}
.footer{left:0;top:950px;width:1138px;height:190px;background:var(--footer)}
.footer-base{left:0;top:1140px;width:1138px;height:60px;background:var(--footer-deep)}
.f-head{top:991px;font-size:16px;color:#fff;font-weight:400}
.f-list{top:1024px;font-size:11.5px;font-weight:300;color:#ddd;line-height:20.5px;list-style:none}
.f-contact{left:576px;top:1036px;font-size:11.5px;font-weight:300;color:#ddd;line-height:20.5px;width:200px}
.news-input{left:848px;top:1031px;width:197px;height:39px;background:#333131;color:#777;font-size:10px;font-style:italic;font-weight:300;padding:0 13px;display:flex;align-items:center}
.news-btn{left:967px;top:1085px;width:78px;height:26px;background:var(--teal);border-radius:2px;color:#fff;font-size:11.5px;display:flex;align-items:center;justify-content:center}
.copyright{left:0;top:1163px;width:1138px;text-align:center;font-size:11.5px;color:#fff;font-weight:300}
</style>
</head>
<body>
<div class="abs top-rule"></div>

<header>
  <div class="abs brand"><span class="brand-dot"></span>Brindal</div>
  <nav class="abs nav">
    <span style="left:523px">HOME</span>
    <span style="left:604px">PLATFORM</span>
    <span style="left:715px">ABOUT</span>
    <span style="left:801px" class="active">CONTACT</span>
    <span style="left:903px">REGISTER</span>
    <span style="left:1007px">LOGIN</span>
  </nav>
</header>

<section>
  <div class="abs hero" role="img" aria-label="Illustration of delivery trucks on a glowing connected map with route pins"></div>
  <svg class="abs hero-arrow" style="left:25px" viewBox="0 0 34 34"><circle cx="17" cy="17" r="15.5" fill="none" stroke="#fff" stroke-width="2"/><path d="M19.5 10 12.5 17 19.5 24" fill="none" stroke="#fff" stroke-width="2"/></svg>
  <svg class="abs hero-arrow" style="left:1072px" viewBox="0 0 34 34"><circle cx="17" cy="17" r="15.5" fill="none" stroke="#fff" stroke-width="2"/><path d="M14.5 10 21.5 17 14.5 24" fill="none" stroke="#fff" stroke-width="2"/></svg>
  <h1 class="abs hero-title">CONTACT US</h1>
  <p class="abs hero-sub">MANAGER OF YOUR DELIVERIES</p>
  <div class="abs hero-shade"></div>
</section>

<main>
  <h2 class="abs section-title">CONTACT <b>US</b></h2>

  <div class="abs field" style="left:93px;top:515px;width:266px;height:39px">Name<svg viewBox="0 0 12 12"><circle cx="6" cy="3.5" r="3"/><path d="M0 12c0-4 2.5-5 6-5s6 1 6 5z"/></svg></div>
  <div class="abs field" style="left:372px;top:515px;width:266px;height:39px">Surname<svg viewBox="0 0 12 12"><circle cx="6" cy="3.5" r="3"/><path d="M0 12c0-4 2.5-5 6-5s6 1 6 5z"/></svg></div>

  <div class="abs field" style="left:93px;top:567px;width:174px;height:39px">Company<svg viewBox="0 0 12 12"><path d="M2 4 6 8 10 4" fill="none" stroke="#666" stroke-width="1.3"/></svg></div>
  <div class="abs field" style="left:279px;top:567px;width:173px;height:39px">Country<svg viewBox="0 0 12 12"><path d="M2 4 6 8 10 4" fill="none" stroke="#666" stroke-width="1.3"/></svg></div>
  <div class="abs field" style="left:464px;top:567px;width:174px;height:39px">State<svg viewBox="0 0 12 12"><path d="M2 4 6 8 10 4" fill="none" stroke="#666" stroke-width="1.3"/></svg></div>

  <div class="abs field" style="left:93px;top:621px;width:266px;height:39px">Email<svg viewBox="0 0 12 12"><path d="M0 2h12v8H0z"/><path d="M0 2 6 7 12 2" fill="none" stroke="#f8f8f8" stroke-width="1.2"/></svg></div>
  <div class="abs field" style="left:372px;top:621px;width:266px;height:39px">Telephone<svg viewBox="0 0 12 12"><path d="M2.5 0.5 4.5 3 3.3 4.6c.8 1.7 2.3 3.2 4 4L8.9 7.4l2.6 2-1.4 2.1C5 11 1 7 .5 1.9z"/></svg></div>

  <div class="abs field msg" style="left:93px;top:673px;width:545px;height:145px">Message<svg viewBox="0 0 12 12"><path d="M9 5v6H1V3h6" fill="none" stroke="#666" stroke-width="1.2"/><path d="M4.5 7.5 5 5.5 10 .5 11.5 2 6.5 7z"/></svg></div>

  <div class="abs submit">Submit Now</div>

  <div class="abs map"><div role="img" aria-label="Road map showing the office location"></div></div>

  <h3 class="abs addr-title">ADDRESS</h3>
  <div class="abs addr-rule"></div>

  <svg class="abs addr-icon" style="top:746px" viewBox="0 0 16 16"><path d="M8 15S3 9.5 3 6a5 5 0 0 1 10 0c0 3.5-5 9-5 9z"/><circle cx="8" cy="6" r="1.7"/></svg>
  <p class="abs addr-item" style="top:745px">Address : 200 Latin words, combined with a handful</p>

  <svg class="abs addr-icon" style="top:793px;fill:var(--teal);stroke:none" viewBox="0 0 16 16"><path d="M3.5 1 6 4.3 4.5 6.2c1 2.2 3 4.2 5.2 5.3L11.7 10 15 12.6 13.2 15C6.5 14.5 1.5 9.5 1 2.6z"/></svg>
  <p class="abs addr-item" style="top:793px">Ph : 5550142377 / 5550169823</p>

  <svg class="abs addr-icon" style="top:824px;width:17px" viewBox="0 0 17 16"><rect x="1" y="2.5" width="15" height="11" rx="1"/><path d="M1.5 3.5 8.5 9 15.5 3.5"/></svg>
  <p class="abs addr-item" style="top:824px">E mail : hello@brindal.example</p>
</main>

<footer>
  <div class="abs footer"></div>
  <h4 class="abs f-head" style="left:97px">COMPANY</h4>
  <ul class="abs f-list" style="left:95px"><li>Support</li><li>Price</li><li>Sign up</li><li>Contact</li></ul>

  <h4 class="abs f-head" style="left:251px">COMMUNITY</h4>
  <ul class="abs f-list" style="left:249px"><li>Guiglines</li><li>Terms and conditions</li><li>privacy policy</li><li>site map</li></ul>

  <h4 class="abs f-head" style="left:437px">FOLLOW US</h4>
  <ul class="abs f-list" style="left:437px"><li>Facebeam</li><li>Chirpline</li><li>Snapgrid</li><li>searchly</li></ul>

  <h4 class="abs f-head" style="left:606px">CONTACT US</h4>
  <p class="abs f-contact">Address : 200 Latin words, combined<br>with a handful<br>Ph : 5550142377 / 5550169823<br>E mail : hello@brindal.example</p>

  <h4 class="abs f-head" style="left:847px">NEWSLETTER</h4>
  <div class="abs news-input">Enter The Mail Id</div>
  <div class="abs news-btn">Send Now</div>

  <div class="abs footer-base"></div>
  <p class="abs copyright">Copyrights@2016Company name all rights reserved</p>
</footer>
</body>
</html>
```